Business Card for Coral Reef Shore Dive Lodge
Kelumpang Beach Resort & Dive Tour Sdn. Bhd.
Bright & Fun-filled
Harudin Bin Sulaiman Taib
QRT Marketing & HR Manager
C27-4, Meranti Square, Jalan Tuaran
88450 Kota Kinabalu, SABAH Malaysia.
kelumpangresort@mailnest.example
572918-K (KPL/LN 4721)
logo vector

```html
<!DOCTYPE html>
<html lang="en">
<head>
<meta charset="utf-8">
<title>Kelumpang Stationery Set</title>
<link href="https://fonts.googleapis.com/css2?family=Cinzel:wght@400;600&family=Lato:wght@400&display=swap" rel="stylesheet">
<style>
:root{
  --backdrop:#e9ddc9;
  --paper:#ffffff;
  --paper-shade:#f3f1ee;
  --bronze:#9c6b47;
  --bronze-light:#c49a76;
  --ink:#3c3c3c;
  --muted:#8a8a8a;
  --card-black:#111111;
  --envelope-grey:#d6d6d8;
  --art-soft:#ece7e2;
}
*{box-sizing:border-box;margin:0;padding:0}
html,body{width:1200px;height:446px;overflow:hidden}
body{background:var(--backdrop);position:relative;font-family:"Lato",sans-serif;color:var(--ink)}
.piece{position:absolute;box-shadow:0 2px 6px rgba(0,0,0,.25)}
.label{position:absolute;font-size:7px;letter-spacing:.5px;color:#7b6650;font-family:"Lato",sans-serif;white-space:nowrap}
.brand{font-family:"Cinzel",serif;font-weight:600;color:var(--bronze);letter-spacing:2px;text-transform:uppercase;display:flex;align-items:center;gap:4px;white-space:nowrap}
.brand .dot{width:6px;height:6px;border-radius:50%;background:var(--bronze);flex:none}
.art{position:absolute;border-radius:40% 40% 30% 30%;background:linear-gradient(160deg,var(--art-soft),rgba(236,231,226,0))}
/* cards */
.card{display:flex;flex-direction:column;align-items:center;justify-content:center;overflow:hidden}
.card-black{background:var(--card-black)}
.card-bronze{background:linear-gradient(135deg,var(--bronze-light),var(--bronze))}
.card .brand{font-size:6px;letter-spacing:1px;gap:2px}
.card .brand .dot{width:3px;height:3px}
.card-front .brand{font-size:9px;letter-spacing:2px;gap:3px}
.card-front .brand .dot{width:4px;height:4px}
.card-lines{font-size:3.5px;color:#fff;line-height:5px;text-align:center;font-family:"Cinzel",serif;white-space:nowrap}
/* letterheads */
.letterhead{background:var(--paper);width:288px;height:403px;top:19px;overflow:hidden}
.letterhead .brand{font-size:13px;position:absolute;top:20px;left:24px}
.letterhead .tagline{position:absolute;top:38px;left:24px;font-size:5px;color:var(--muted);font-family:"Cinzel",serif;letter-spacing:1px;white-space:nowrap}
.letterhead .contact{position:absolute;top:18px;left:184px;font-size:4px;line-height:6px;color:var(--muted);white-space:nowrap}
.lh-centered .brand{left:50%;transform:translateX(-50%);top:34px;font-size:14px}
.lh-centered .tagline{left:0;right:0;text-align:center;top:52px}
.footer-band{position:absolute;left:14px;right:14px;bottom:14px;height:9px;background:var(--bronze);display:flex;justify-content:space-around;align-items:center;font-size:3.5px;color:#fff}
/* envelopes */
.envelope{left:797px;width:403px;overflow:hidden}
.envelope .brand{position:absolute;left:50%;transform:translateX(-50%);font-size:10px}
.env-bronze{top:0;height:96px;background:var(--paper)}
.env-grey{top:91px;height:101px;background:var(--paper-shade)}
.env-white{top:180px;height:96px;background:var(--paper)}
.env-front{top:264px;width:331px;height:144px;background:var(--paper)}
.env-front .brand{left:22px;transform:none;top:22px;font-size:12px}
.env-front .tagline{position:absolute;left:22px;top:38px;font-size:4.5px;color:var(--muted);font-family:"Cinzel",serif;letter-spacing:1px;white-space:nowrap}
.env-front .contact{position:absolute;left:22px;top:48px;font-size:4px;line-height:6px;color:var(--muted);white-space:nowrap}
</style>
</head>
<body>

<!-- Business cards -->
<p class="label" style="left:12px;top:163px">Business Card Identity</p>
<div class="piece card card-black" style="left:12px;top:175px;width:60px;height:58px">
  <span class="brand"><span class="dot"></span>Kelumpang</span>
</div>
<div class="piece card card-bronze" style="left:72px;top:175px;width:67px;height:58px">
  <div class="card-lines">Your Name Here<br>Position Title<br>Street Address Line<br>City, State<br>Email Address</div>
</div>
<p class="label" style="left:12px;top:236px">Business Card Front</p>
<div class="piece card card-black card-front" style="left:12px;top:246px;width:127px;height:56px">
  <span class="brand"><span class="dot"></span>Kelumpang</span>
</div>
<p class="label" style="left:12px;top:305px">Business Card Back</p>

<!-- Letterhead option 1 -->
<section class="piece letterhead" style="left:163px">
  <div class="brand"><span class="dot"></span>Kelumpang</div>
  <div class="tagline">Coral Reef Shore Dive Lodge</div>
  <div class="contact">
    Street Address Line One<br>
    City, Postcode, Country<br>
    Email Address Here<br>
    Registration No.
  </div>
  <div class="art" role="img" aria-label="Faint mermaid illustration" style="left:40px;top:220px;width:140px;height:170px"></div>
</section>
<p class="label" style="left:270px;top:430px">Letterhead Option 1</p>

<!-- Letterhead option 2 -->
<section class="piece letterhead lh-centered" style="left:475px">
  <div class="brand"><span class="dot"></span>Kelumpang</div>
  <div class="tagline">Coral Reef Shore Dive Lodge</div>
  <div class="art" role="img" aria-label="Faint mermaid illustration" style="left:80px;top:150px;width:150px;height:160px"></div>
  <div class="footer-band"><span>Address</span><span>Street</span><span>City</span><span>Reg. No.</span></div>
</section>
<p class="label" style="left:582px;top:430px">Letterhead Option 2</p>

<!-- Envelopes -->
<div class="piece envelope env-bronze">
  <svg width="403" height="96" style="position:absolute;left:0;top:0"><path d="M0 0 H403 V40 L201 88 L0 40 Z" fill="var(--bronze)"/></svg>
  <div class="art" role="img" aria-label="Small mermaid illustration" style="left:300px;top:8px;width:46px;height:34px;background:linear-gradient(160deg,rgba(255,255,255,.55),rgba(255,255,255,0))"></div>
</div>
<div class="piece envelope env-grey">
  <svg width="403" height="101" style="position:absolute;left:0;top:0"><path d="M0 0 H403 V30 L201 78 L0 30 Z" fill="var(--envelope-grey)"/></svg>
  <div class="brand" style="top:50px"><span class="dot"></span>Kelumpang</div>
</div>
<div class="piece envelope env-white">
  <svg width="403" height="96" style="position:absolute;left:0;top:0"><path d="M0 0 H403 V26 L201 74 L0 26 Z" fill="var(--envelope-grey)"/></svg>
  <div class="brand" style="top:48px"><span class="dot"></span>Kelumpang</div>
</div>
<div class="piece envelope env-front">
  <div class="brand"><span class="dot"></span>Kelumpang</div>
  <div class="tagline">Coral Reef Shore Dive Lodge</div>
  <div class="contact">Street Address Line One<br>City, Postcode, Country</div>
  <div class="art" role="img" aria-label="Faint mermaid illustration" style="left:200px;top:40px;width:100px;height:100px"></div>
</div>
<p class="label" style="left:930px;top:430px">Envelope Option</p>

</body>
</html>
```